Web Banner Design Project - Yield Compass

We would like to develop a "branding image" (banner) for the home page of a new website. The concept image is shown on the attached PDF. (The PDF should be rotated counterclockwise 90 degrees once for proper orientation.)
The image shows multiple financial (i.e. stock market, for example) chart lines.
The idea for the concept is "making sense of the noise". So, the image begins on the left with a bunch of different chart lines all intertwined. The words and numbers on the left are intended to represent inputs into the investment decision process. Then, as we move to the right on the image, the result becomes more orderly and clear, and the chart lines consolidate and move upwards. This represents the positive benefit (i.e. financial gain) from understanding the underlying Yield Compass.
The main idea behind the concept is a "Symphony". If all of the instruments in the Symphony are not working together, the result is chaos. But when all instruments are working together in harmony, the Symphony produces beautiful music. So. we would also like to incorporate "symphony" symbols into the design, such as musical notes or instruments for example.
Some general stock market images can be found here:
http://www.plumavista-imagery.com/browse?q=stock+market+graph
Here are some individual examples of stock market images:
http://www.plumavista-imagery.com/item-580112934/stock-market-graph-on-a-tablet-computer.html?ref=q7Lm-1-1
http://www.plumavista-imagery.com/item-581447026/financial-graph-of-investment-growth.html?ref=q7Lm-5-47
http://www.plumavista-imagery.com/item-38906215/illustration-of-the-red-stock-market-chart.html?ref=q7Lm-1-53
http://www.plumavista-imagery.com/item-579032618/euro-money-background-with-trade-charts-and-stock-stats.html?ref=q7Lm-5-0
The following image shows a bright light at the upper right corner. We would like to also possibly incorporate something like this, which would represent the "light at the end of the tunnel".
http://www.plumavista-imagery.com/item-61870493/stock-market-ticker-boards-circular-arranged-as-a-tunnel-with-light-at-the-end.html?ref=q7Lm-3-70
These images are for reference only to help communicate the look and feel.
Thank you for your help.
Investment

```html
<!DOCTYPE html>
<html lang="en">
<head>
<meta charset="utf-8">
<title>Yield Compass – Symphony Banner</title>
<link rel="stylesheet" href="https://fonts.googleapis.com/css2?family=Doto:wght@700;900&display=swap">
<style>
  :root{
    --bg-deep:#06239a;
    --bg-mid:#0a4fd6;
    --bg-glow:#1a7cf0;
    --sheet-light:#3ff2ff;
    --sheet-mid:#25c8f4;
    --sheet-edge:#2a9fe8;
    --staff:#2a6fd0;
    --ink-dark:#0b1a8c;
    --ink-blue:#1d4fe0;
    --ink-green:#4fe86a;
    --label:#1c40c8;
    --label-faint:#2c84e6;
  }
  html,body{margin:0;padding:0;overflow:hidden;}
  .banner{
    position:relative;width:1200px;height:486px;overflow:hidden;
    background:
      radial-gradient(ellipse 70% 60% at 85% 15%, var(--bg-glow) 0%, transparent 70%),
      linear-gradient(160deg, var(--bg-mid) 0%, var(--bg-deep) 100%);
    font-family:"Doto", monospace;
  }
  .banner svg{position:absolute;inset:0;}
  .reading{position:absolute;margin:0;font-weight:900;white-space:nowrap;letter-spacing:1px;}
  .reading--volume{left:228px;top:108px;font-size:38px;color:var(--label-faint);opacity:.55;}
  .reading--demand{left:710px;top:138px;font-size:30px;color:var(--label);}
  .reading--sentiment{left:516px;top:184px;font-size:14px;color:var(--label);}
  .reading--supply{left:420px;top:352px;font-size:14px;color:var(--label);transform:rotate(-4deg);}
</style>
</head>
<body>
<main class="banner">
  <svg width="1200" height="486" viewBox="0 0 1200 486">
    <defs>
      <linearGradient id="sheet-fill" x1="0" y1="0" x2="1" y2="0.3">
        <stop offset="0" stop-color="var(--sheet-mid)"/>
        <stop offset="0.5" stop-color="var(--sheet-light)"/>
        <stop offset="1" stop-color="var(--sheet-edge)"/>
      </linearGradient>
      <clipPath id="sheet-clip">
        <path d="M42,72 Q600,40 1120,118 Q1195,230 1160,378 Q600,384 60,468 Q10,270 42,72Z"/>
      </clipPath>
    </defs>

    <path class="sheet-shadow" d="M50,84 Q600,54 1128,130 Q1204,244 1168,392 Q600,398 68,482 Q18,282 50,84Z" fill="#021060" opacity=".55"/>
    <path class="sheet" d="M42,72 Q600,40 1120,118 Q1195,230 1160,378 Q600,384 60,468 Q10,270 42,72Z" fill="url(#sheet-fill)"/>

    <g class="staff" clip-path="url(#sheet-clip)" stroke="var(--staff)" stroke-width="1.5" fill="none" opacity=".55">
      <path d="M40,62 Q600,70 1180,150"/>
      <path d="M40,122 Q600,120 1180,180"/>
      <path d="M40,182 Q600,170 1180,215"/>
      <path d="M40,262 Q600,230 1180,255"/>
      <path d="M40,352 Q600,300 1180,300"/>
    </g>

    <g class="music-marks" clip-path="url(#sheet-clip)" fill="var(--staff)" opacity=".35">
      <rect role="img" aria-label="Treble clef symbol" x="95" y="40" width="70" height="400" rx="35"/>
      <rect role="img" aria-label="Musical note" x="505" y="130" width="26" height="46" rx="10"/>
      <rect role="img" aria-label="Musical note" x="560" y="100" width="40" height="60" rx="12"/>
      <rect role="img" aria-label="Musical note" x="605" y="100" width="28" height="110" rx="12"/>
      <rect role="img" aria-label="Musical notes" x="935" y="158" width="36" height="30" rx="8"/>
    </g>

    <g class="chart-lines" clip-path="url(#sheet-clip)" fill="none" stroke-width="3" stroke-linejoin="miter">
      <polyline class="chart-line chart-line--green" stroke="var(--ink-green)"
        points="80,140 105,90 125,130 145,60 170,120 190,70 215,160 230,100 250,230 270,150 290,240 310,180 335,300 360,200 385,310 410,240 440,330 465,250 495,300 520,240 550,290 580,250 610,290 640,260 670,290 700,270 730,285 760,265 790,280 820,260 850,275 880,255 910,262 940,245 970,252 1000,240 1030,245 1060,232 1090,236 1110,222"/>
      <polyline class="chart-line chart-line--blue" stroke="var(--ink-blue)"
        points="85,270 110,330 130,240 150,300 170,200 195,280 215,170 240,260 265,180 290,300 315,240 340,350 370,260 395,330 425,250 455,310 485,240 515,285 545,260 575,300 605,265 640,290 670,265 700,282 735,262 765,280 795,258 825,272 855,250 885,262 915,245 945,255 975,240 1005,246 1035,232 1065,238 1095,222 1110,215"/>
      <polyline class="chart-line chart-line--dark" stroke="var(--ink-dark)"
        points="95,420 120,330 140,380 160,280 185,350 205,250 230,340 255,290 280,400 305,320 335,290 365,350 395,240 425,310 455,260 485,330 515,235 545,285 575,250 605,275 640,232 670,262 700,242 730,258 760,232 790,252 820,228 850,242 880,226 910,236 940,218 970,228 1000,212 1030,218 1060,204 1090,212 1110,210"/>
    </g>
  </svg>

  <p class="reading reading--volume">VOL 13</p>
  <p class="reading reading--demand">DEMAND 26.57</p>
  <p class="reading reading--sentiment">Sentiment 42</p>
  <p class="reading reading--supply">SUPPLY 24.60</p>
</main>
</body>
</html>
```